Real Estate "For Sale" Sign for a Colorado Real Estate Company

I need a sign for my Real Estate Company and the size needs to be 24inches by 24inches when printed on metal.
Logo is attached and would like to keep it modern and simple. We are a small town and I am not looking for a new age, industrial design. The concept needs to have the following attributes:

- Logo placed on sign
- Text "For Sale"
- Text "Reid Calloway" and my phone number "720-555-0143" (I would need any font package you use so that I can edit my number if that changes)
- Text "www.reid-calloway.example"
Im open to other attributes as well!

Target Market(s)

General Public driving around town.

Industry/Entity Type

Real Estate Agent

Requirements
Must have
• Logo and the colors must not be too busy. Contact Info very clear.

```html
<!DOCTYPE html>
<html lang="en">
<head>
<meta charset="utf-8">
<title>For Sale Sign – Elk Ridge Realty</title>
<link rel="stylesheet" href="https://fonts.googleapis.com/css2?family=Cinzel:wght@500;600&family=Open+Sans:wght@600;700&display=swap">
<style>
  :root {
    --brand-blue: #0f80c1;
    --brand-navy: #1a4566;
    --rule-black: #231f20;
    --phone-grey: #414042;
    --paper: #ffffff;
  }
  * { margin: 0; padding: 0; box-sizing: border-box; }
  html, body {
    width: 1188px;
    height: 1200px;
    overflow: hidden;
    background: var(--paper);
  }
  .sign {
    position: relative;
    width: 1188px;
    height: 1200px;
    background: var(--paper);
    font-family: "Cinzel", serif;
  }
  .band {
    position: absolute;
    left: 0;
    width: 100%;
    background: var(--brand-blue);
    color: var(--paper);
    display: flex;
    align-items: center;
    justify-content: center;
  }
  .band--top { top: 0; height: 232px; }
  .band--bottom { bottom: 0; height: 168px; }
  .rule {
    position: absolute;
    left: 0;
    width: 100%;
    height: 6px;
    background: var(--rule-black);
  }
  .rule--top { top: 243px; }
  .rule--bottom { top: 1017px; }
  .headline {
    font-family: "Cinzel", serif;
    font-weight: 500;
    font-size: 196px;
    line-height: 1;
    letter-spacing: 2px;
    padding-top: 10px;
  }
  .company-name {
    position: absolute;
    top: 470px;
    left: 0;
    width: 100%;
    text-align: center;
    font-family: "Cinzel", serif;
    font-weight: 600;
    font-size: 74px;
    line-height: 1;
    color: var(--brand-navy);
  }
  .agent-name {
    position: absolute;
    top: 728px;
    left: 0;
    width: 100%;
    text-align: center;
    font-family: "Cinzel", serif;
    font-weight: 600;
    font-size: 84px;
    line-height: 1;
    color: var(--brand-navy);
  }
  .agent-phone {
    position: absolute;
    top: 868px;
    left: 0;
    width: 100%;
    display: flex;
    align-items: center;
    justify-content: center;
    gap: 18px;
    font-family: "Open Sans", sans-serif;
    font-weight: 700;
    font-size: 88px;
    line-height: 1;
    color: var(--phone-grey);
  }
  .agent-phone svg { width: 76px; height: 76px; flex: none; }
  .website {
    font-family: "Open Sans", sans-serif;
    font-weight: 600;
    font-size: 62px;
    letter-spacing: 5px;
    line-height: 1;
  }
</style>
</head>
<body>
  <main class="sign">
    <header class="band band--top">
      <h1 class="headline">For Sale</h1>
    </header>
    <div class="rule rule--top"></div>

    <p class="company-name">Elk Ridge Realty</p>

    <p class="agent-name">Reid Calloway</p>
    <p class="agent-phone">
      <svg viewBox="0 0 76 76" aria-hidden="true">
        <circle cx="38" cy="38" r="34" fill="none" stroke="#0f80c1" stroke-width="4"/>
        <path d="M30 18 l8 12 -5 5 c3 6 6 9 11 12 l5 -5 12 8 -4 7 c-16 -1 -33 -18 -34 -34 z" fill="none" stroke="#0f80c1" stroke-width="3.5" stroke-linejoin="round"/>
      </svg>
      <span>720-555-0143</span>
    </p>

    <div class="rule rule--bottom"></div>
    <footer class="band band--bottom">
      <p class="website">www.reid-calloway.example</p>
    </footer>
  </main>
</body>
</html>
```